Warehouse Surplus Flyer

2 Sided Flyer to be used in print and online for short, unadvertised sale to pharmacies for prescription vials. Please feel free to edit wordiness.

Side One:
WE PASS ALONG THE SAVINGS TO YOU
WAREHOUSE SURPLUS UNADVERTISED OFFER
BY INVITATION ONLY TO YOU

We have a acquired a surplus, with our supplier, on ALL AMBER color and ALL with CHILD RESISTANT CAPS and we would like to pass along the savings to you, as we need to make room for other inventory.

Normally these vials sell for over $50 a case! We are going to move these vials at very special pricing.

Very cost-effective, Quality Vials

KTR Supply provides pharmacy vials in the independent pharmacy market and conditioned toner cartridges in pharmacies and several other vertical markets.
Please call us at 888-412-5096 and we will be happy to work with you directly.

ktrsupplyco.com

This is not an advertised sale. Offer Ends September 30, 2013*.

2nd Side:
VIAL SIZE QUANTITY PER CASE CASES AVAILABLE
8 Dram 410 50
10 Dram 360 50
13 Dram 310 500
16 Dram 260 500
20 Dram 270 500
30 Dram 240 500
40 Dram 200 500
60 Dram 140 100

During this offer to move inventory, we are selling these at 30% to 50% off our already discounted rate, based on volume.

Quantities: (*While Supplies Last)
• 1 to 500 cases will be sold at 30% off our discounted price! $28 Per Case
• 501 to 1000 cases will be sold at 40% our discounted price! $25 Per Case
• Over 1000 cases will be sold at 50% our discounted price! $22 Per Case

We also have great pricing on conditioned toner cartridges. You can also view our line of products and prices on www.ktrsupplyco.com.

Please call us at 888-412-5096 and we will be happy to work with you directly. This is not an advertised sale.
Updates

Deadline IS AUGUST 28TH! SEPTEMBER SALE.

Target Market(s)

Independent Pharmacies

Industry/Entity Type

Online

Requirements
Must have
• 3 color or Less front side, 2 Sided Flyer
• Backside can be 1 Color
• Phone Number
• web address
• sales expiration date
Nice to have
• graphic call outs to gain attention

```html
<!DOCTYPE html>
<html lang="en">
<head>
<meta charset="utf-8">
<title>KTR Supply – Warehouse Surplus Flyer</title>
<link rel="stylesheet" href="https://fonts.googleapis.com/css2?family=Jura:wght@500;700&family=Russo+One&display=swap">
<style>
  :root {
    --stage: #3a3a3a;
    --paper: #ffffff;
    --blue: #1a66d6;
    --navy: #0c2a86;
    --green: #1fc43a;
    --lime: #7ed321;
    --deep-green: #0b7a2a;
    --red: #e0201c;
    --ink: #1b1b1b;
    --link-blue: #1a66d6;
    --vial: #c77a2a;
  }
  * { box-sizing: border-box; margin: 0; padding: 0; }
  html, body { width: 1200px; height: 900px; overflow: hidden; }
  body {
    background: var(--stage);
    font-family: "Jura", sans-serif;
    color: var(--ink);
    position: relative;
  }
  .flyer {
    position: absolute;
    top: 70px;
    width: 520px;
    height: 760px;
    background: var(--paper);
    overflow: hidden;
  }
  .flyer--front { left: 45px; }
  .flyer--back { left: 635px; }
  .flyer__art { position: absolute; inset: 0; }
  .vial-photo {
    position: absolute;
    width: 56px; height: 36px;
    border-radius: 6px;
    background: linear-gradient(180deg, #e09a4a, var(--vial));
  }
  .brand {
    position: absolute;
    top: 32px; left: 24px;
    display: flex; align-items: center; gap: 10px;
    font-family: "Russo One", sans-serif;
    font-size: 26px;
    color: #fff;
  }
  .brand__dot { width: 14px; height: 14px; border-radius: 50%; background: #fff; }
  .headline {
    position: absolute;
    top: 262px; left: 20px; right: 20px;
    text-align: center;
    font-family: "Russo One", sans-serif;
    color: var(--red);
    font-size: 19px;
    line-height: 1.35;
  }
  .copy {
    position: absolute;
    left: 30px; right: 30px;
    font-size: 13px;
    font-weight: 500;
    line-height: 1.35;
  }
  .copy p { margin-bottom: 11px; }
  .copy strong { font-weight: 700; }
  .accent-red { color: var(--red); font-weight: 700; }
  .accent-blue { color: var(--link-blue); font-weight: 700; }
  .justify { text-align: justify; }
  .front-copy { top: 355px; }
  .site {
    position: absolute;
    bottom: 22px; right: 20px;
    display: flex; align-items: center; gap: 10px;
    color: #fff;
    font-size: 24px;
    font-weight: 700;
  }
  .site svg { width: 26px; height: 26px; }
  .size-table {
    position: absolute;
    top: 185px; left: 40px; right: 30px;
  }
  .size-table__head {
    font-family: "Russo One", sans-serif;
    color: var(--red);
    font-size: 13px;
    text-align: center;
    margin-bottom: 6px;
  }
  .size-table__cols { display: flex; justify-content: space-around; }
  .size-table table { border-collapse: collapse; font-size: 15px; font-weight: 700; }
  .size-table td { padding: 0 5px; line-height: 1.3; }
  .back-copy {
    top: 305px; left: 24px; right: 18px;
    font-size: 12.5px;
    line-height: 1.3;
  }
  .back-copy p { margin-bottom: 10px; }
  .back-copy ul { list-style: none; margin-bottom: 10px; }
  .back-copy li { white-space: nowrap; }
  .back-copy li::before { content: "· "; }
  .back-copy .closing { color: var(--red); }
</style>
</head>
<body>

<section class="flyer flyer--front">
  <svg class="flyer__art" viewBox="0 0 520 760" aria-hidden="true">
    <path d="M0 0H520V120C380 125 160 150 0 250Z" fill="var(--navy)"/>
    <path d="M0 0H520V100C380 100 150 125 0 225Z" fill="var(--blue)"/>
    <circle cx="232" cy="95" r="11" fill="#fff"/>
    <circle cx="268" cy="88" r="16" fill="#fff"/>
    <circle cx="315" cy="78" r="21" fill="#fff"/>
    <circle cx="372" cy="66" r="28" fill="#fff"/>
    <path d="M0 760V690C180 710 380 680 520 620V760Z" fill="var(--deep-green)"/>
    <path d="M0 760V710C180 726 380 700 520 645V760Z" fill="var(--green)"/>
    <circle cx="150" cy="735" r="12" fill="#fff"/>
    <circle cx="188" cy="731" r="16" fill="#fff"/>
    <circle cx="232" cy="727" r="20" fill="#fff"/>
    <circle cx="60" cy="712" r="38" fill="#fff"/>
  </svg>
  <div class="vial-photo" role="img" aria-label="Amber pharmacy vials" style="left:32px;top:694px;"></div>

  <div class="brand"><span>KTR Supply LLC.</span><span class="brand__dot"></span></div>

  <h1 class="headline">WE PASS ALONG THE SAVINGS TO YOU<br>WAREHOUSE SURPLUS UNADVERTISED OFFER<br>BY INVITATION ONLY TO YOU</h1>

  <div class="copy front-copy">
    <p>We have a acquired a surplus, with our supplier, on <strong>ALL AMBER</strong> color and <strong>ALL</strong> with <strong>CHILD RESISTANT CAPS</strong> and we would like to pass along the savings to you, as we need to make room for other inventory.</p>
    <p>Normally these vials sell for over <strong>$50</strong> a case! We are going to move these vials at very special pricing.</p>
    <p class="accent-red">Very cost-effective, Quality Vials</p>
    <p class="justify"><span class="accent-blue">KTR Supply</span> provides pharmacy vials in the independent pharmacy market and conditioned toner cartridges in pharmacies and several other vertical markets.</p>
    <p>Please call us at <span class="accent-blue">888-412-5096</span> and we will be happy to work with you directly.</p>
    <p>This is not an advertised sale. Offer Ends <span class="accent-red">September 30, 2013*</span>.</p>
  </div>

  <div class="site">
    <svg viewBox="0 0 28 28" fill="none" stroke="#fff" stroke-width="2"><circle cx="14" cy="14" r="12"/><ellipse cx="14" cy="14" rx="5" ry="12"/><path d="M2 14H26M4 8H24M4 20H24"/></svg>
    <span>ktrsupplyco.com</span>
  </div>
</section>

<section class="flyer flyer--back">
  <svg class="flyer__art" viewBox="0 0 520 760" aria-hidden="true">
    <path d="M0 0H520V125C360 120 130 140 0 215Z" fill="var(--deep-green)"/>
    <path d="M0 0H520V105C360 98 130 118 0 190Z" fill="var(--lime)"/>
    <circle cx="300" cy="40" r="11" fill="#fff"/>
    <circle cx="338" cy="38" r="16" fill="#fff"/>
    <circle cx="388" cy="36" r="21" fill="#fff"/>
    <circle cx="456" cy="34" r="28" fill="#fff"/>
    <path d="M0 760V645C160 665 380 640 520 565V760Z" fill="var(--navy)"/>
    <path d="M0 760V665C170 685 380 662 520 590V760Z" fill="var(--blue)"/>
    <circle cx="62" cy="690" r="36" fill="#fff"/>
    <circle cx="128" cy="725" r="16" fill="#fff"/>
    <circle cx="170" cy="728" r="13" fill="#fff"/>
    <circle cx="205" cy="730" r="10" fill="#fff"/>
    <rect x="30" y="290" width="470" height="3" fill="var(--blue)"/>
    <rect x="30" y="294" width="470" height="2" fill="var(--green)"/>
  </svg>
  <div class="vial-photo" role="img" aria-label="Amber pharmacy vials" style="left:34px;top:672px;"></div>

  <div class="brand" style="top:24px;"><span>KTR Supply LLC.</span><span class="brand__dot"></span></div>

  <div class="size-table">
    <div class="size-table__head">VIAL SIZE QUANTITY PER CASE CASES AVAILABLE</div>
    <div class="size-table__cols">
      <table>
        <tr><td>8 Dram</td><td>410</td><td>50</td></tr>
        <tr><td>10 Dram</td><td>360</td><td>50</td></tr>
        <tr><td>13 Dram</td><td>310</td><td>500</td></tr>
        <tr><td>16 Dram</td><td>260</td><td>500</td></tr>
      </table>
      <table>
        <tr><td>20 Dram</td><td>270</td><td>500</td></tr>
        <tr><td>30 Dram</td><td>240</td><td>500</td></tr>
        <tr><td>40 Dram</td><td>200</td><td>500</td></tr>
        <tr><td>60 Dram</td><td>140</td><td>100</td></tr>
      </table>
    </div>
  </div>

  <div class="copy back-copy">
    <p>During this offer to move inventory, we are selling these at 30% to 50% off our already discounted rate, based on volume.</p>
    <p style="margin-bottom:0">Quantities: (*While Supplies Last)</p>
    <ul>
      <li><span class="accent-blue">1 to 500 cases</span> will be sold at <strong>30%</strong> off our discounted price! <span class="accent-red">$28</span> Per Case</li>
      <li><span class="accent-blue">501 to 1000 cases</span> will be sold at <strong>40%</strong> our discounted price! <span class="accent-red">$25</span> Per Case</li>
      <li><span class="accent-blue">Over 1000 cases</span> will be sold at <strong>50%</strong> our discounted price! <span class="accent-red">$22</span> Per Case</li>
    </ul>
    <p>We also have great pricing on conditioned toner cartridges. You can also view our line of products and prices on www.ktrsupplyco.com.</p>
    <p>Please call us at <span class="accent-blue">888-412-5096</span> and we will be happy to work with you directly.</p>
    <p class="closing">This is not an advertised sale.</p>
  </div>

  <div class="site">
    <svg viewBox="0 0 28 28" fill="none" stroke="#fff" stroke-width="2"><circle cx="14" cy="14" r="12"/><ellipse cx="14" cy="14" rx="5" ry="12"/><path d="M2 14H26M4 8H24M4 20H24"/></svg>
    <span>ktrsupplyco.com</span>
  </div>
</section>

</body>
</html>
```